Harbourline Electrical limited business card design

I need a business card made up it must be double sided with just my logo and some graphic one side and then on the reverse a little description of services I provide along with my email address phone number and face book and instagram handles
I already had a logo designed by pixel guild and the social media pack so I’m thinking to use the social media design as the main image
Services I provide are: domestic commercial industrial sub contract from bathroom's and kitchen’s to outside lights and sockets no job to big or to small

Industry/Entity Type

Electrician/construction industry

Contact Information for Business Card

Email address: harbourlineelectrical@mailvane.net mobile number: 07854326190 fb: Harbourline Electrical insta: @harbourlineelectrical

Font styles to use
Sans Serif

Colors
0094D4
00A9DD
6FCCEA
C7EBF8
E9F6FB
FFF300
FFF600
FEFA6F
FFFEC7
FFFEE8

Requirements
Must have
• Double sided, fb and insta handles contact info, domestic commercial industrial sub contract
Nice to have
• From bathroom's and kitchen’s to outside outside lights and sockets no job to big or to small

```html
<!DOCTYPE html>
<html lang="en">
<head>
<meta charset="utf-8">
<title>Harbourline Electrical – Business Card</title>
<link href="https://fonts.googleapis.com/css2?family=Montserrat:wght@800&family=Roboto:wght@400;500;700&display=swap" rel="stylesheet">
<style>
  :root {
    --stage: #5f5f60;
    --card-dark: #141414;
    --card-light: #f3f3f4;
    --card-light-edge: #dcdcde;
    --brand-blue: #0a8fd0;
    --name-blue: #1677bd;
    --gold: #f0b130;
    --gold-deep: #e39e22;
    --ink: #222222;
  }
  * { margin: 0; padding: 0; box-sizing: border-box; }
  html, body {
    width: 900px; height: 1200px; overflow: hidden;
    background: var(--stage);
  }
  .canvas { position: relative; width: 900px; height: 1200px; }

  .card {
    position: absolute; left: 149px; width: 602px; height: 387px;
    overflow: hidden;
    box-shadow: 0 8px 18px rgba(0,0,0,.35);
  }

  /* Front */
  .card-front { top: 200px; background: var(--card-dark); }
  .corner-decoration { position: absolute; }
  .corner-decoration.top-left { left: 0; top: 0; width: 240px; height: 205px; }
  .corner-decoration.bottom-right { right: 0; bottom: 0; width: 245px; height: 205px; }

  .front-mark {
    position: absolute; left: 250px; top: 121px;
    width: 108px; height: 108px; border-radius: 50%;
    border: 5px solid var(--brand-blue);
  }
  .front-wordmark {
    position: absolute; left: 0; right: 0; top: 242px;
    text-align: center;
    font-family: "Montserrat", sans-serif; font-weight: 800;
    color: var(--brand-blue);
  }
  .front-wordmark .line-main { display: block; font-size: 33px; line-height: 1; }
  .front-wordmark .line-sub {
    display: block; font-size: 15px; letter-spacing: 11px;
    margin-top: 10px; padding-left: 11px; line-height: 1;
  }

  /* Back */
  .card-back {
    top: 613px;
    background: radial-gradient(ellipse at 42% 45%, #ffffff 0%, var(--card-light) 45%, var(--card-light-edge) 100%);
    font-family: "Roboto", sans-serif;
  }
  .contact-block { position: absolute; left: 44px; top: 113px; }
  .person-name { font-size: 25px; font-weight: 700; color: var(--name-blue); line-height: 1; }
  .person-role { font-size: 14px; color: var(--ink); margin-top: 6px; letter-spacing: .3px; }
  .contact-list { list-style: none; margin-top: 10px; }
  .contact-list li {
    display: flex; align-items: center; gap: 5px;
    font-size: 15px; color: var(--ink); letter-spacing: .6px;
    height: 22.5px;
  }
  .contact-icon { width: 12px; height: 12px; flex: none; }

  .back-mark {
    position: absolute; left: 360px; top: 121px;
    width: 166px; height: 166px; border-radius: 50%;
    border: 6px solid var(--brand-blue);
    display: flex; align-items: center; justify-content: center;
    text-align: center;
    font-family: "Roboto", sans-serif; font-weight: 700;
    color: var(--brand-blue); font-size: 17px; line-height: 1.25;
  }

  .services {
    position: absolute; left: 44px; width: 514px; top: 332px;
    display: flex; justify-content: space-between; align-items: center;
    font-size: 17.5px; font-weight: 700; color: var(--brand-blue);
  }
  .services .divider { width: 3px; height: 22px; background: var(--gold); }
</style>
</head>
<body>
<main class="canvas">

  <section class="card card-front">
    <svg class="corner-decoration top-left" viewBox="0 0 240 205" role="img" aria-label="Lightning bolt over a curved Greek key border">
      <defs>
        <linearGradient id="tlFill" x1="0" y1="0" x2="1" y2="1">
          <stop offset="0" stop-color="#1a86c4"/>
          <stop offset="0.45" stop-color="#e9ad2f"/>
          <stop offset="1" stop-color="#e9a52a"/>
        </linearGradient>
      </defs>
      <polygon points="0,0 234,0 8,202 0,150" fill="url(#tlFill)"/>
    </svg>

    <div class="front-mark" aria-hidden="true"></div>
    <h1 class="front-wordmark">
      <span class="line-main">HARBOURLINE</span>
      <span class="line-sub">ELECTRICAL</span>
    </h1>

    <svg class="corner-decoration bottom-right" viewBox="0 0 245 205" role="img" aria-label="Lightning bolt over a curved Greek key border">
      <defs>
        <linearGradient id="brFill" x1="0" y1="1" x2="1" y2="0">
          <stop offset="0" stop-color="#eeb02e"/>
          <stop offset="0.6" stop-color="#f3c23a"/>
          <stop offset="1" stop-color="#1a86c4"/>
        </linearGradient>
      </defs>
      <polygon points="245,0 245,205 0,205" fill="url(#brFill)"/>
    </svg>
  </section>

  <section class="card card-back">
    <div class="contact-block">
      <h2 class="person-name">Marten Holloway</h2>
      <p class="person-role">Owner</p>
      <ul class="contact-list">
        <li>
          <svg class="contact-icon" viewBox="0 0 24 24" aria-hidden="true"><path fill="#1677bd" d="M6.6 10.8a15.1 15.1 0 0 0 6.6 6.6l2.2-2.2c.3-.3.7-.4 1-.2 1.1.4 2.3.6 3.6.6.6 0 1 .4 1 1V20c0 .6-.4 1-1 1A17 17 0 0 1 3 4c0-.6.4-1 1-1h3.5c.6 0 1 .4 1 1 0 1.3.2 2.5.6 3.6.1.3 0 .7-.2 1z"/></svg>
          07854326190
        </li>
        <li>
          <svg class="contact-icon" viewBox="0 0 24 24" aria-hidden="true"><path fill="#1677bd" d="M2 5h20v14H2z"/><path fill="none" stroke="#fff" stroke-width="2" d="M2 5l10 8 10-8"/></svg>
          harbourlineelectrical@mailvane.net
        </li>
        <li>
          <svg class="contact-icon" viewBox="0 0 24 24" aria-hidden="true"><circle cx="12" cy="12" r="11" fill="#1677bd"/></svg>
          Harbourline Electrical
        </li>
        <li>
          <svg class="contact-icon" viewBox="0 0 24 24" aria-hidden="true"><circle cx="12" cy="12" r="11" fill="#1677bd"/></svg>
          @harbourlineelectrical
        </li>
      </ul>
    </div>

    <div class="back-mark">Harbourline<br>Electrical</div>

    <div class="services">
      <span>DOMESTIC</span><span class="divider"></span>
      <span>COMMERCIAL</span><span class="divider"></span>
      <span>INDUSTRIAL</span><span class="divider"></span>
      <span>SUB CONTRACT</span>
    </div>
  </section>

</main>
</body>
</html>
```